Web Design for Solar Energy Consultancy Company

~ May 3, 2017 Update ~
As our project is rapidly progressing towards its completion, we started building up the list of designs that attracted the most of the team's attention. Additional submittals are still most welcome. Before submitting your proposal, however, we can recommend to review the concepts that received 4 stars as these are the ones that, in our opinion, most closely match the brief's requirements. Thank you!!
~ April 30, 2017 Update ~
The project deadline has been extended to attract a broader design community and to better tailor the final design to the requirements of the project.
A "light", "clean" (minimalistic), professionally looking, unique design is expected. Please, try to avoid industry cliches. Also, please use green, which became another industry cliche, with great caution. The brief provides minimum details to foster creativity. With the same notion in mind, the page content information is not provided.
Thank you for your feedback and support of the project!!
~ April 22, 2017 Update ~
Additional comments after starting receiving more designs:
- your attention to the brief's requirements will be highly appreciated. It is expected that the design is unique - standard, commonly used, images, formats and approaches do not fall under this category. There is no need to "bombard" with slightly different variations of the same design. It is expected that a conceptual (preliminary) design is submitted first, and, after it is reviewed (each design will receive a star rating and, if the star rating is greater than 3, a detailed feedback), the requested changes are implemented. We believe this will allow to approach the design process more efficiently and safe additional time to both the Designers's Community and our company. Thank you for understanding.
Clarification, please submit two variations of a design:
1) 1 page "business card" design that the company will be able to use during its startup stage;
2) the fully functional design (as per the requirements outlined below) for the company to transition to after the start-up period is over. Same design principles as developed for option 1 should be used for this variation.
Additional clarification, please note that the news block will not require images (at least during the start-up stage). It is envisioned to be a news feeder.
~ April 21, 2017 Update ~
Preliminary comments after receiving first designs:
- please try to create a unique design, using common elements wisely. Though such solar energy "attributes" as a solar panel or a bulb are very well recognized and allow quickly identify the nature of the business, they also became so common that in many cases a design may seem very similar to the one of others (Oh!, I've already seen this... effect).
- please try to introduce the company's logo unobtrusively. The size and position of the logo should clearly identify the company, but the message should be subtle, the logo should not distract from the main design. Brask's swoosh did not need to occupy have the screen.
- please use the green color with caution as it was with the company's logo. True, it is a green energy. But there is no need for the color to "scream" about it. Use the amount of green and its tone (avoid acid green) wisely.
--------------------------------------------------------------------------------
1. Main Goal
Develop a website that can represent the company to the industry stakeholders and become its "business card" during the start-up stage.
2. Secondary Goal
Develop a structure of a fully functional website that the "business card" design can eventually be transformed to staying consistent with the original design principles.
3. Key Audience
Varolu Corp. is providing consulting and technical services in the area of Solar Energy. The industry stakeholders include project developers, financial community, governmental bodies, OEMs, and competition.
4. Site Map
- HOME
• About
• Services
• Solar Energy
• News
• Contacts
• Social Media
- SERVICES*
- PROJECTS*
- FINANCE*
- TRAINING*
- SOLAR (ENERGY)*
* Maybe inactive / partially functional during the start-up stage.
5. Technical Specifications
Online brochure website during the start-up stage with a capability to be eventually transformed to a fully functional website while preserving the original design principles.
The design to be appealing, "light", professional, and with an intuitive and easy to navigate interface. Modern coding principles supporting efficiency and security to be utilized. Newest industry trends in website coding will be welcome.
The website to be designed so that it would fit well a computer, tablet, or mobile phone screen of any size. Cross-platform functionality to be taken into consideration to ensure that the website is fully functional on any platform.
Company's logo has already been designed and will be shared with the short-listed designers during the final design stage.
6. Interaction
The website will provide information about the company, our services, and projects. In addition, the industry insight, accumulated knowledge, and most recent trends are planned to be shared with stakeholders and attract and retain the audience.
Interaction with designers during the website development is envisioned to go through the following steps:
a) conceptual design - to be proposed by a designer originally. All conceptual designs will be reviewed and a feedback provided to pre-selected designers;
b) (preliminary and) final design - depending on the level of additional changes required can be broken into two steps. After discussing preliminary designs, company images will be provided to the selected finalists, who will compete with their final proposals.
7. Industry Stakeholders
- https://www.quellbrin.com/power/solar-power.- http://www.pakortavon.com/
- http://www.vellitrazo.com/about/company/
- https://www.oruxem.com/energy/index.html
8. Budget
Defined by the project.
9. Timescale
Defined by the project.
12. Additional Info
- No copy-cats, standard graphics, or cliches please!
- Additional information / clarifications will be gladly provided upon request.
- This specification may be updated throughout the project to reflect discussions with / changes proposed by the Designers community.

```html
<!DOCTYPE html>
<html lang="en">
<head>
<meta charset="utf-8">
<title>Varolu Corp. – Solar Energy Consulting</title>
<link href="https://fonts.googleapis.com/css2?family=Raleway:ital,wght@0,400;0,500;0,600;0,700;0,800;1,400;1,600;1,700&family=Open+Sans:wght@400;600&display=swap" rel="stylesheet">
<style>
:root{
  --green:#3aad3a;
  --green-dark:#1c6b33;
  --green-deep:#145a29;
  --yellow:#ffc600;
  --ink:#333333;
  --page:#e4e4e4;
  --white:#ffffff;
  --rule:#d9d9d9;
  --date-gray:#7a7a7a;
}
*{box-sizing:border-box;margin:0;padding:0}
html,body{width:1200px;height:2378px;overflow:hidden}
body{background:var(--page);font-family:'Raleway',sans-serif;color:var(--ink);position:relative}
.abs{position:absolute}

.header-band{left:0;top:0;width:1200px;height:745px;background:linear-gradient(160deg,#1f7a3a 0%,#3aa04f 45%,#2b8a44 70%,#1a6a33 100%)}
.brand{display:flex;align-items:center;gap:12px}
.brand-mark{width:40px;height:40px;border-radius:50%;background:var(--yellow)}
.brand-name{font-family:'Raleway',sans-serif;font-weight:700;font-size:38px;letter-spacing:2px;color:var(--white)}
.header-brand{left:82px;top:36px}
.header-phone{left:920px;top:40px;display:flex;align-items:center;gap:28px;color:var(--white);font-family:'Open Sans',sans-serif;font-size:21px}
.social{display:flex;gap:7px}
.social span{width:25px;height:25px;border-radius:50%;background:#e9e9e9;display:block}
.header-social{left:988px;top:86px}

.main-nav{left:63px;top:135px;width:1072px;height:55px;background:var(--yellow);display:flex;align-items:center;font-size:13.5px;font-weight:500;color:#222;text-transform:uppercase}
.main-nav .home{position:absolute;left:24px;top:16px}
.main-nav .item{position:absolute;top:19px}
.main-nav .search{position:absolute;left:1023px;top:16px}

.hero{left:63px;top:190px;width:1072px;height:479px;background:linear-gradient(115deg,#2c2b26 0%,#4a4538 40%,#6b5f45 70%,#3e3a33 100%)}
.hero-copy{left:118px;top:312px;color:var(--white)}
.hero-kicker{font-size:27px;font-weight:400}
.hero-kicker b{font-weight:800}
.hero-title{font-size:57px;font-weight:800;color:var(--yellow);letter-spacing:1px;line-height:1;margin-top:6px}
.hero-text{font-family:'Open Sans',sans-serif;font-size:13px;line-height:21px;width:500px;margin-top:16px}
.btn{display:inline-block;font-size:12px;font-weight:600;text-transform:uppercase;text-align:center}
.btn-outline{left:119px;top:496px;width:112px;height:35px;line-height:31px;border:2px solid var(--yellow);color:var(--yellow)}
.btn-solid{left:239px;top:496px;width:111px;height:35px;line-height:35px;background:var(--yellow);color:#222}

.content{left:63px;top:669px;width:1072px;height:1078px;background:var(--white)}
.hero-shadow{left:140px;top:669px;width:920px;height:30px;background:radial-gradient(ellipse at top,rgba(0,0,0,.28),rgba(0,0,0,0) 70%)}

.section-title{display:flex;align-items:center;gap:8px;font-size:28px;font-weight:400;color:#333}
.section-title b{font-weight:700;color:var(--green)}
.leaf{width:26px;height:26px}

.about-title{left:97px;top:750px}
.about-text{left:97px;top:805px;width:532px;font-size:13.2px;line-height:21.4px;text-align:justify;hyphens:auto;-webkit-hyphens:auto;color:#444}
.btn-green{left:97px;top:1024px;width:111px;height:32px;line-height:32px;background:var(--green);color:var(--white);font-size:12px;font-weight:600;text-align:center}

.tiles{left:727px;top:693px;width:376px;height:375px;display:grid;grid-template-columns:187px 187px;grid-template-rows:186px 186px;gap:2px}
.tile{display:flex;flex-direction:column;align-items:center;justify-content:center;color:var(--white);text-align:center}
.tile h3{font-size:21px;font-weight:700;letter-spacing:.5px}
.tile p{font-size:13px}
.tile-brand{background:var(--white)}
.tile-brand .brand-name{color:#333;font-size:30px}
.tile-brand .brand-mark{width:32px;height:32px}
.tile-projects{background:linear-gradient(160deg,#4cbf4c,#36a53a)}
.tile-finance{background:linear-gradient(160deg,#53c050,#3aa43a)}
.tile-training{background:linear-gradient(160deg,#ffc933,#f5b800)}

.divider{left:97px;top:1138px;width:1008px;height:4px;background:var(--rule)}

.solar-title{left:97px;top:1172px}
.solar-card{left:97px;top:1225px;width:333px;height:415px;background:var(--green)}
.solar-visual{left:111px;top:1238px;width:304px;height:149px;background:linear-gradient(90deg,#e8f3fb,#cfe6f5 45%,#e7f5d6)}
.solar-text{left:114px;top:1410px;width:300px;font-size:12.8px;line-height:21.6px;color:var(--white);text-align:justify;hyphens:auto;-webkit-hyphens:auto}
.btn-readmore{left:312px;top:1588px;width:98px;height:35px;line-height:31px;border:1.5px solid var(--white);color:var(--white);font-size:12.5px;font-weight:700;text-align:center}

.news-title{left:512px;top:1172px}
.news-list{left:509px;top:1239px;width:593px}
.news-item{position:relative;height:99px;border-bottom:1.5px dashed #cfcfcf;display:flex;align-items:center}
.news-item.active{background:#eeeeee;height:106px}
.date{position:absolute;left:12px;top:20px;width:61px;height:62px;background:var(--date-gray);color:var(--white);text-align:center;font-family:'Open Sans',sans-serif;line-height:1}
.news-item.active .date{background:var(--yellow);top:25px}
.date .m{font-size:10.5px;display:block;padding-top:5px}
.date .d{font-size:29px;font-weight:600;display:block}
.date .y{font-size:10.5px;display:block;padding-top:1px}
.news-body{position:absolute;left:101px;top:26px;width:470px}
.news-item.active .news-body{top:30px}
.news-body h4{font-size:13.6px;font-weight:700;font-style:italic;color:#333}
.news-body p{font-family:'Open Sans',sans-serif;font-size:11.2px;line-height:18px;color:#888;margin-top:5px}

.testimonials{left:63px;top:1747px;width:1072px;height:388px;background:linear-gradient(135deg,#ffcb12 0%,#ffc400 55%,#f6bb00 100%)}
.t-title{left:63px;top:1808px;width:1072px;text-align:center;color:var(--white);font-size:27px;font-weight:700}
.t-rule{left:533px;top:1850px;width:140px;height:5px;border-top:1.5px solid rgba(255,255,255,.8);border-bottom:1.5px solid rgba(255,255,255,.8)}
.avatar{left:217px;top:1905px;width:98px;height:98px;border-radius:50%;background:#d8d2c8;border:5px solid var(--white);box-shadow:0 3px 8px rgba(0,0,0,.25)}
.t-quote{left:348px;top:1920px;width:670px;color:var(--white);font-size:12.8px;font-style:italic;line-height:23px}
.t-quote .q{font-size:26px;font-style:normal;font-weight:700;line-height:0;vertical-align:-6px}
.t-name{left:370px;top:1994px;color:var(--white);font-size:16.5px;font-weight:700}
.t-dots{left:507px;top:2070px;display:flex;gap:7px}
.t-dots span{width:43px;height:2px;background:rgba(255,255,255,.85)}

.footer{left:0;top:2135px;width:1200px;height:243px;background:var(--green-dark)}
.footer-bar{left:0;top:2344px;width:1200px;height:34px;background:var(--green-deep);color:#d8e8d8;font-size:11.5px;text-align:center;line-height:34px}
.vrule{top:2160px;width:1px;height:170px;background:rgba(255,255,255,.15)}
.footer-brand{left:92px;top:2162px}
.footer-brand .brand-name{font-size:32px}
.footer-brand .brand-mark{width:36px;height:36px}
.contact-line{left:98px;display:flex;align-items:flex-start;gap:14px;color:var(--white);font-size:11.5px;line-height:16px}
.f-head{color:var(--white);font-size:15px;font-weight:700;text-transform:uppercase}
.f-link{color:var(--white);font-size:11.5px}
.f-link::before{content:"›";margin-right:10px}
.f-note{left:634px;top:2216px;width:250px;color:var(--white);font-size:11.5px;line-height:18px}
.f-input{left:636px;top:2267px;width:174px;height:32px;background:#2b7d42;color:#cfe6d2;font-size:11px;line-height:32px;padding-left:12px}
.f-submit{left:810px;top:2267px;width:89px;height:32px;background:var(--yellow);color:#222;font-size:11px;font-weight:700;line-height:32px;text-align:center}
.footer-social{left:958px;top:2212px;display:flex;gap:4px}
.footer-social span{width:33px;height:33px;border-radius:50%;background:var(--white);border:2px solid #cfcfcf;display:block}
</style>
</head>
<body>

<div class="abs header-band" role="img" aria-label="Green-tinted photo of a solar panel field"></div>

<div class="abs brand header-brand"><span class="brand-mark"></span><span class="brand-name">VAROLU</span></div>

<div class="abs header-phone">
  <svg width="12" height="20" viewBox="0 0 12 20"><rect x="1" y="1" width="10" height="18" rx="2" fill="none" stroke="#fff" stroke-width="1.6"/><rect x="3" y="4" width="6" height="8" fill="#fff"/></svg>
  <span>(014) 772 5308</span>
</div>
<div class="abs social header-social"><span></span><span></span><span></span><span></span></div>

<nav class="abs main-nav">
  <svg class="home" width="24" height="22" viewBox="0 0 24 22"><path d="M12 1 L23 11 H20 V21 H14 V14 H10 V21 H4 V11 H1 Z" fill="#111"/></svg>
  <span class="item" style="left:89px">About Us</span>
  <span class="item" style="left:191px">Services</span>
  <span class="item" style="left:292px">Social Energy</span>
  <span class="item" style="left:433px">Projects</span>
  <span class="item" style="left:544px">Finance</span>
  <span class="item" style="left:642px">Training</span>
  <span class="item" style="left:749px">News</span>
  <span class="item" style="left:837px">Contacts</span>
  <svg class="search" width="22" height="22" viewBox="0 0 22 22"><circle cx="8.5" cy="8.5" r="6.5" fill="none" stroke="#111" stroke-width="2.4"/><line x1="13.5" y1="13.5" x2="20" y2="20" stroke="#111" stroke-width="3" stroke-linecap="round"/></svg>
</nav>

<div class="abs hero" role="img" aria-label="Photo of a technician installing a solar panel on a roof"></div>
<div class="abs hero-copy">
  <div class="hero-kicker">Providing <b>100%</b> Harmless</div>
  <div class="hero-title">SOLAR ENERGY</div>
  <p class="hero-text">Lorem Ipsum is simply dummy text of the printing and typesetting industry. Lorem Ipsum has been the industry's standard dummy text ever</p>
</div>
<span class="abs btn btn-outline">Know More</span>
<span class="abs btn btn-solid">Book Now</span>

<div class="abs content"></div>
<div class="abs hero-shadow"></div>

<h2 class="abs section-title about-title">
  <svg class="leaf" viewBox="0 0 26 26"><path d="M3 24 C3 10 10 3 24 3 C22 8 18 10 12 11 C8 13 5 18 3 24 Z" fill="#777"/></svg>
  About <b>VAROLU</b>
</h2>
<p class="abs about-text">Lorem Ipsum is simply dummy text of the printing and typesetting industry. Lorem Ipsum has been the industry's standard dummy text ever since the 1500s, when an unknown printer took a galley of type and scrambled it to make a type specimen book. It has sur&shy;vived not only five centuries, but also the leap into electronic typesetting, remaining es&shy;sentially unchanged. It was popularised in the 1960s with the release of Letraset sheets containing Lorem Ipsum passages, and more recently with desktop publishing software like Aldus PageMaker including versions of Lorem Ipsum.</p>
<span class="abs btn-green">KNOW MORE</span>

<div class="abs tiles">
  <div class="tile tile-brand"><div class="brand"><span class="brand-mark"></span><span class="brand-name">VAROLU</span></div></div>
  <div class="tile tile-projects" role="img" aria-label="Green-tinted photo of completed solar projects"><h3>PROJECTS</h3><p>We have done so far</p></div>
  <div class="tile tile-finance" role="img" aria-label="Green-tinted photo of a seedling growing from coins"><h3>FINANCE</h3><p>For best &amp; latest technology</p></div>
  <div class="tile tile-training" role="img" aria-label="Yellow-tinted photo of a training session"><h3>TRAINING</h3><p>We provide for better results</p></div>
</div>

<div class="abs divider"></div>

<h2 class="abs section-title solar-title">
  <svg class="leaf" viewBox="0 0 26 26"><path d="M3 24 C3 10 10 3 24 3 C22 8 18 10 12 11 C8 13 5 18 3 24 Z" fill="#777"/></svg>
  Solar <b>ENERGY</b>
</h2>
<div class="abs solar-card"></div>
<div class="abs solar-visual" role="img" aria-label="Illustration of a light bulb, a solar panel, the sun and a green leaf"></div>
<p class="abs solar-text">Lorem Ipsum is simply dummy text of the printing and typesetting industry. Lorem Ipsum has been the industry's standard dummy text ever since the 1500s, when an unknown printer took a galley of type and scrambled it to make a type specimen book. It has survived not only five centuries, but also the leap into electronic typesetting, remain&shy;ing essentially unchanged.</p>
<span class="abs btn-readmore">Read More &gt;&gt;</span>

<h2 class="abs section-title news-title">
  <svg class="leaf" viewBox="0 0 26 26"><path d="M3 24 C3 10 10 3 24 3 C22 8 18 10 12 11 C8 13 5 18 3 24 Z" fill="#777"/></svg>
  Company <b>NEWS</b>
</h2>
<div class="abs news-list">
  <article class="news-item active">
    <div class="date"><span class="m">MAY</span><span class="d">03</span><span class="y">2017</span></div>
    <div class="news-body"><h4>It is a long established fact that a reader will be distracted</h4><p>Many desktop publishing packages and web page editors now use Lorem Ipsum as their default model text.</p></div>
  </article>
  <article class="news-item">
    <div class="date"><span class="m">MAY</span><span class="d">03</span><span class="y">2017</span></div>
    <div class="news-body"><h4>It is a long established fact that a reader will be distracted</h4><p>Many desktop publishing packages and web page editors now use Lorem Ipsum as their default model text.</p></div>
  </article>
  <article class="news-item">
    <div class="date"><span class="m">MAY</span><span class="d">03</span><span class="y">2017</span></div>
    <div class="news-body"><h4>It is a long established fact that a reader will be distracted</h4><p>Many desktop publishing packages and web page editors now use Lorem Ipsum as their default model text.</p></div>
  </article>
  <article class="news-item" style="border-bottom:none">
    <div class="date"><span class="m">MAY</span><span class="d">03</span><span class="y">2017</span></div>
    <div class="news-body"><h4>It is a long established fact that a reader will be distracted</h4><p>Many desktop publishing packages and web page editors now use Lorem Ipsum as their default model text.</p></div>
  </article>
</div>

<div class="abs testimonials"></div>
<h2 class="abs t-title">What Our Clients Say</h2>
<div class="abs t-rule"></div>
<div class="abs avatar" role="img" aria-label="Client portrait photo"></div>
<p class="abs t-quote"><span class="q">“</span> Lorem Ipsum is simply dummy text of the printing and typesetting industry. Lorem Ipsum has been the industry's standard dummy text ever since the 1500s, when an unknown printer took a galley of type and scrambled it to make a type specimen book. <span class="q">”</span></p>
<div class="abs t-name">Dorian Vell, New York City</div>
<div class="abs t-dots"><span></span><span></span><span></span><span></span></div>

<footer class="abs footer"></footer>
<div class="abs vrule" style="left:315px"></div>
<div class="abs vrule" style="left:586px"></div>
<div class="abs vrule" style="left:927px"></div>

<div class="abs brand footer-brand"><span class="brand-mark"></span><span class="brand-name">VAROLU</span></div>
<div class="abs contact-line" style="top:2234px">
  <svg width="12" height="16" viewBox="0 0 12 16"><path d="M6 0 C2.7 0 0 2.6 0 5.8 C0 10 6 16 6 16 C6 16 12 10 12 5.8 C12 2.6 9.3 0 6 0 Z" fill="#fff"/><circle cx="6" cy="5.8" r="2.2" fill="#1c6b33"/></svg>
  <span>Area Name, Street No 1234,<br>City, State-456778</span>
</div>
<div class="abs contact-line" style="top:2280px">
  <svg width="10" height="16" viewBox="0 0 10 16"><rect x="1" y="1" width="8" height="14" rx="1.5" fill="none" stroke="#fff" stroke-width="1.4"/><rect x="2.5" y="3" width="5" height="7" fill="#fff"/></svg>
  <span>(014) 772 53081</span>
</div>
<div class="abs contact-line" style="top:2310px">
  <svg width="14" height="11" viewBox="0 0 14 11"><rect x="0.7" y="0.7" width="12.6" height="9.6" fill="none" stroke="#fff" stroke-width="1.4"/><path d="M1 1 L7 6 L13 1" fill="none" stroke="#fff" stroke-width="1.4"/></svg>
  <span>info@varolucorp.com</span>
</div>

<h3 class="abs f-head" style="left:363px;top:2174px">Quick Links</h3>
<span class="abs f-link" style="left:368px;top:2219px">Home</span>
<span class="abs f-link" style="left:368px;top:2246px">Services</span>
<span class="abs f-link" style="left:368px;top:2273px">Finance</span>
<span class="abs f-link" style="left:368px;top:2300px">Training</span>
<span class="abs f-link" style="left:472px;top:2219px">About Us</span>
<span class="abs f-link" style="left:472px;top:2246px">Solar Energy</span>
<span class="abs f-link" style="left:472px;top:2273px">Projects</span>
<span class="abs f-link" style="left:472px;top:2300px">Contacts</span>

<h3 class="abs f-head" style="left:634px;top:2174px">Newsletter Signup</h3>
<p class="abs f-note">Please enter your email address to get our latest newsletters</p>
<div class="abs f-input">Email Address</div>
<div class="abs f-submit">SUBSCRIBE</div>

<h3 class="abs f-head" style="left:965px;top:2174px">Get Connected</h3>
<div class="abs footer-social"><span></span><span></span><span></span><span></span></div>

<div class="abs footer-bar">© 2017 Varolu Corp. All Rights Reserved &nbsp;&nbsp; Sitemap &nbsp;|&nbsp; Privacy Policy</div>

</body>
</html>
```